Harborlight Unity Collective Sponsorship

FULL PROJECT DESCRIPTION PROVIDED IN PDF AND WORD DOC (UPLOADED).

Harborlight Unity Collective is looking for an updated sponsorship package design – included in the shared information is our sponsorship packaged used in 2017, 2018, and 2019.

The mission of Harborlight Unity Collective is to create opportunities for integrating and promoting visibility for the lesbian. gay, bisexual and transgender community; promoting equal rights and diversity through public education and the arts; provide safe opportunities and venues for people to come out with the ability to express and celebrate their sexual identities.

Some images (because of their size) are not allowed to be uploaded... use the following link to access the full library of images, reference documents, and the full outline: https://files.vexorabox.net/shared/7qTmW3zK9-4rbLnYcP2sVdHgE6uJaXf0N?mode=view

Sponsorship packet design details:
Final file type: .pdf and/or .ai/.eps
Orientation: Preferably landscape but not opposed to a portrait design.
Page count: estimated 6 with current content (not opposed to 8 pages)
Size: 8.5”x11”
Full bleed

Images:
Images for this design are shared in a folder “images for use in sponsorship packet” – please feel free to choose them as you see fit and we can make any notes after the first draft.

Creative Reference:
Additionally, provided are a few sponsorship packages that we like and feel that you might be able to take inspiration from – these are in a folder named “sponsorship packets we like”
Updates

I've updated all of the details of this project and would like to have completed asap. Thank you.

Target Market(s)

Primarily our target market is local and regional businesses that are interested in supporting GlowFair through sponsorship or might be interested in advertising opportunities.

Industry/Entity Type

LGBT

Font styles to use
Serif
Sans Serif

Colors

Designer to choose colors to be used in the design.

Requirements
Must have
• All sponsorship details

```html
<!DOCTYPE html>
<html lang="en">
<head>
<meta charset="utf-8">
<title>Harborlight Unity Collective – Sponsorship Packet</title>
<link rel="stylesheet" href="https://fonts.googleapis.com/css2?family=Poppins:wght@600;700;800&family=Open+Sans:wght@400;600&display=swap">
<style>
  :root{
    --board:#eceef2;
    --board-light:#f7f8fa;
    --paper:#ffffff;
    --purple:#5b3a94;
    --purple-deep:#4a2d7d;
    --red:#ec3b46;
    --orange:#f47b2a;
    --yellow:#f9c22e;
    --blue:#3d7fd6;
    --green:#3fae5b;
    --ink:#3b3b45;
    --muted:#8a8a96;
  }
  *{margin:0;padding:0;box-sizing:border-box}
  html,body{width:1200px;height:3008px;overflow:hidden}
  body{background:var(--board);font-family:"Open Sans",Arial,sans-serif;color:var(--ink);position:relative}
  .board-band{position:absolute;inset:0}
  .page{position:absolute;background:var(--paper);overflow:hidden;box-shadow:0 10px 30px rgba(40,40,70,.14)}
  .page-label{position:absolute;left:70px;font:700 15px "Poppins",sans-serif;letter-spacing:2px;color:#55555f}
  .photo{position:absolute}
  p{font-size:9.5px;line-height:1.55;margin-bottom:9px}
  h2,h3{font-family:"Poppins",sans-serif}

  /* cover */
  .cover{left:420px;top:40px;width:360px;height:466px}
  .cover-photo{left:100px;top:40px;width:160px;height:160px;border-radius:50%;
    background:radial-gradient(circle at 40% 40%,#e9a7b9,#8c5aa8 55%,#3d4c8a);
    box-shadow:0 0 0 8px #fff,0 0 0 16px var(--red)}
  .cover-ring{position:absolute;left:76px;top:16px;width:208px;height:208px;border-radius:50%;
    background:conic-gradient(var(--red),var(--orange),var(--yellow),var(--green),var(--blue),var(--purple),var(--red));
    -webkit-mask:radial-gradient(circle,transparent 96px,#000 97px);mask:radial-gradient(circle,transparent 96px,#000 97px)}
  .cover-badge{position:absolute;left:232px;top:172px;width:72px;height:72px;border-radius:50%;background:var(--red);
    color:#fff;text-align:center;font:800 17px/1 "Poppins",sans-serif;padding-top:18px}
  .cover-badge small{display:block;font:600 7px/1.2 "Open Sans",sans-serif;margin-top:4px}
  .cover-brand{position:absolute;left:34px;top:300px;display:flex;align-items:center;gap:8px;font:700 15px "Poppins",sans-serif;color:var(--purple)}
  .cover-brand i{width:12px;height:12px;border-radius:50%;background:var(--purple);display:block}
  .cover-sub{position:absolute;left:34px;top:330px;font:600 9px "Open Sans",sans-serif;color:var(--muted);letter-spacing:1px;text-transform:uppercase}
  .cover-stripes{position:absolute;left:0;right:0;bottom:0;height:56px;display:flex;flex-direction:column}
  .cover-stripes span{flex:1}

  /* page 1 */
  .p1{left:308px;top:560px;width:584px;height:752px}
  .p1-photo{left:0;top:0;width:584px;height:310px;background:linear-gradient(160deg,#8e939c,#c85b4e 45%,#e8b14a 70%,#6c7383)}
  .p1-title{position:absolute;left:32px;top:330px;width:250px;font:800 40px/1.05 "Poppins",sans-serif;color:var(--purple)}
  .p1-left{position:absolute;left:32px;top:430px;width:250px}
  .p1-right{position:absolute;left:310px;top:330px;width:244px}
  .salute{font-weight:600;color:var(--purple)}
  .sign{font-weight:600}
  .p1-dot{position:absolute;right:-40px;bottom:-40px;width:170px;height:170px;border-radius:50%;background:var(--yellow)}
  .p1-ring{position:absolute;right:60px;bottom:70px;width:60px;height:60px;border-radius:50%;border:10px solid var(--orange)}
  .p1-small{position:absolute;left:260px;top:280px;width:60px;height:60px;border-radius:50%;background:var(--orange)}

  /* page 2 */
  .p2{left:308px;top:1350px;width:584px;height:752px}
  .p2-photo{left:0;top:0;width:584px;height:200px;background:linear-gradient(90deg,#d23a5a,#f28c3a 30%,#f5d14a 50%,#47a86a 68%,#3c7bd0 84%,#7447a6)}
  .p2-hero{position:absolute;left:30px;top:22px;font:700 30px "Poppins",sans-serif;color:#fff}
  .p2-circle1{left:370px;top:150px;width:180px;height:180px;border-radius:50%;border:6px solid #fff;background:radial-gradient(circle at 40% 35%,#9fc9ea,#4f86c2 60%,#2d4e8a)}
  .p2-circle2{left:40px;top:390px;width:190px;height:190px;border-radius:50%;border:6px solid #fff;background:radial-gradient(circle at 50% 40%,#f2b8c6,#c45f8c 55%,#6a3a82)}
  .p2-h1{position:absolute;left:30px;top:222px;width:320px;font:700 20px/1.2 "Poppins",sans-serif;color:var(--red)}
  .p2-b1{position:absolute;left:30px;top:280px;width:320px}
  .p2-h2{position:absolute;left:270px;top:410px;width:290px;font:700 20px/1.2 "Poppins",sans-serif;color:var(--purple)}
  .p2-b2{position:absolute;left:270px;top:468px;width:290px}
  .p2-yellow{position:absolute;left:340px;top:340px;width:34px;height:34px;border-radius:50%;background:var(--yellow)}
  .p2-band{position:absolute;left:0;bottom:0;width:584px;height:130px;background:var(--purple);color:#fff;display:flex;gap:26px;padding:32px 30px}
  .p2-band h3{font-size:12px;line-height:1.2;width:90px;flex:none;color:var(--yellow)}
  .p2-band p{color:#eee6fb}

  /* page 3 */
  .p3{left:308px;top:2150px;width:584px;height:752px}
  .p3-title{position:absolute;left:30px;top:34px;font:800 34px "Poppins",sans-serif;
    background:linear-gradient(90deg,var(--red),var(--orange),var(--yellow),var(--green),var(--blue),var(--purple));
    -webkit-background-clip:text;background-clip:text;color:transparent}
  .p3-price{position:absolute;left:262px;top:44px;font:700 20px "Poppins",sans-serif;color:var(--ink)}
  .p3-price b{color:var(--muted);font-weight:600;margin-right:8px}
  .p3-list{position:absolute;left:30px;top:110px;width:310px;list-style:none}
  .p3-list li{font-size:9.5px;line-height:1.5;padding:5px 0 5px 16px;border-bottom:1px solid #ececf1;position:relative}
  .p3-list li::before{content:"";position:absolute;left:0;top:10px;width:7px;height:7px;border-radius:50%;background:var(--red)}
  .p3-note{position:absolute;left:30px;top:400px;width:310px}
  .p3-photo{left:370px;top:0;width:214px;height:752px;background:linear-gradient(180deg,#3b3f6b,#c0567a 40%,#e8a14c 70%,#4a6aa8)}
  .p3-inset{left:330px;top:60px;width:150px;height:150px;border-radius:50%;border:6px solid #fff;background:radial-gradient(circle at 45% 40%,#bfe0f3,#5b94c9 60%,#2c4f86)}
  .p3-red{position:absolute;left:400px;top:390px;width:150px;height:150px;border-radius:50%;background:var(--red);color:#fff;text-align:center;padding-top:40px;font-family:"Poppins",sans-serif}
  .p3-red strong{display:block;font-size:34px;font-weight:800;line-height:1}
  .p3-red span{font-size:18px;font-weight:700}
  .p3-ring{position:absolute;left:-90px;bottom:-90px;width:240px;height:240px;border-radius:50%;border:30px solid var(--red)}
</style>
</head>
<body>
  <svg class="board-band" width="1200" height="3008" aria-hidden="true">
    <polygon points="0,520 1200,300 1200,620 0,860" fill="#f6f7f9"/>
    <polygon points="0,1900 1200,1650 1200,1900 0,2150" fill="#f6f7f9"/>
  </svg>

  <section class="page cover">
    <div class="cover-ring"></div>
    <div class="photo cover-photo" role="img" aria-label="Crowd celebrating at the pride parade"></div>
    <div class="cover-badge">2020<small>Sponsorship Opportunities</small></div>
    <div class="cover-brand"><i></i>Harborlight Unity Collective</div>
    <div class="cover-sub">Sponsorship &amp; Advertising Opportunities</div>
    <div class="cover-stripes"><span style="background:var(--purple)"></span><span style="background:var(--yellow)"></span><span style="background:var(--red)"></span></div>
  </section>

  <div class="page-label" style="top:930px">PAGE 1</div>
  <section class="page p1">
    <div class="photo p1-photo" role="img" aria-label="Parade participant with rainbow flags on a city street"></div>
    <div class="p1-small"></div>
    <h2 class="p1-title">Thank you, Sponsor!</h2>
    <div class="p1-left">
      <p class="salute">Dear Harborlight Unity Collective Supporter,</p>
      <p>Thank you for taking the time to consider a sponsorship package for this year's celebration. Your support keeps our festival free, open and welcoming to everyone in our community.</p>
      <p>Each June we gather thousands of neighbors, families and visitors for a parade, a night festival and a full weekend of music, art and conversation. None of it happens without partners like you.</p>
    </div>
    <div class="p1-right">
      <p>Sponsors help us fund safe venues, youth programs, and public education throughout the year. Your name stands beside a mission of visibility, equality and pride.</p>
      <p>Inside you will find sponsorship levels, benefits and advertising options. Our team is happy to build a package that fits your goals.</p>
      <p class="sign">With gratitude,<br>Board of Directors</p>
    </div>
    <div class="p1-ring"></div>
    <div class="p1-dot"></div>
  </section>

  <div class="page-label" style="top:1720px">PAGE 2</div>
  <section class="page p2">
    <div class="photo p2-photo" role="img" aria-label="Rainbow flag waving over the festival crowd"></div>
    <h2 class="p2-hero">Pride comes in all colors</h2>
    <div class="photo p2-circle1" role="img" aria-label="Festival goer waving a flag"></div>
    <h3 class="p2-h1">Support this community &amp; promote your business</h3>
    <div class="p2-b1"><p>Our GlowFair festival draws large crowds from across the region. Sponsoring places your business in front of an engaged, loyal audience that values inclusion.</p></div>
    <div class="p2-yellow"></div>
    <div class="photo p2-circle2" role="img" aria-label="Friends celebrating at the festival"></div>
    <h3 class="p2-h2">Build customer awareness and loyalty</h3>
    <div class="p2-b2"><p>LGBTQ+ consumers remember and reward the brands that stand with them. Show your support all year long.</p></div>
    <div class="p2-band">
      <h3>Audience Snapshot</h3>
      <p>More than forty thousand attendees visit over two days, with strong reach across social media, print and local broadcast partners.</p>
    </div>
  </section>

  <div class="page-label" style="top:2520px">PAGE 3</div>
  <section class="page p3">
    <div class="photo p3-photo" role="img" aria-label="Aerial view of the parade route at dusk"></div>
    <div class="photo p3-inset" role="img" aria-label="Crowd gathered by the waterfront"></div>
    <h2 class="p3-title">PRESENTING</h2>
    <div class="p3-price"><b>|</b>$25,000</div>
    <ul class="p3-list">
      <li>Logo on all printed festival materials</li>
      <li>Premier stage banner placement</li>
      <li>Recognition from the main stage</li>
      <li>Full page ad in the festival guide</li>
      <li>Two vendor booths in a prime location</li>
      <li>Twenty VIP lounge passes</li>
      <li>Featured posts on all social channels</li>
      <li>Named partner in press releases</li>
    </ul>
    <div class="p3-note"><p>Presenting sponsors receive top billing for the entire weekend and the right of first refusal for next year.</p></div>
    <div class="p3-red"><strong>RED</strong><span>$15,000</span></div>
    <div class="p3-ring"></div>
  </section>
</body>
</html>
```